Wine Bottle Label for Cora Whitlow California Wine

This will be a wine bottle label. The wine is produced from grapes from our family farm. Images at bottom are some of same ones in high resolution

Cora Whitlow
Reserve Pinot Noir
Clarksburg 2023
Estate Grown (in cursive)

We would like to have a view from above, looking down from the levee there is a slough (wing of a river) running behind it, it looks down over vineyards, a big wood barn, a giant Oak Tree beyond the barn. There are beautiful sunsets there in the distance. Many birds fly over the vineyards including small black birds (as shown in one photo). Please use what you can from these suggestions to make a label. We will need a small image for back label and wording on it.

Other font styles liked:
• Wine bottle fonts

Requirements
Must have
• Wording mentioned . An Oak Tree with images of the vines and a sunset
Nice to have
• Flock of black birds flying in the sky

```html
<!DOCTYPE html>
<html lang="en">
<head>
<meta charset="utf-8">
<title>Cora Whitlow Reserve Pinot Noir Label</title>
<link rel="stylesheet" href="https://fonts.googleapis.com/css2?family=Pinyon+Script&family=Marcellus+SC&family=Cinzel:wght@500&family=Kaushan+Script&display=swap">
<style>
  :root {
    --backdrop: #e8e8e8;
    --paper: #fbfbfa;
    --ink: #1c1c1c;
    --ink-soft: #3a3a3a;
    --gold: #c99a2e;
    --gold-light: #f0cf6a;
    --gold-deep: #a97a18;
    --scene-light: #d9d9d9;
    --scene-mid: #a6a6a6;
    --scene-dark: #5c5c5c;
  }
  * { margin: 0; padding: 0; box-sizing: border-box; }
  html, body {
    width: 1200px;
    height: 800px;
    overflow: hidden;
    background: var(--backdrop);
  }
  .canvas {
    position: relative;
    width: 1200px;
    height: 800px;
  }
  .label {
    position: absolute;
    left: 315px;
    top: 40px;
    width: 570px;
    height: 720px;
    background: var(--paper);
    box-shadow: 0 2px 10px rgba(0,0,0,0.08);
  }
  .label__rule {
    position: absolute;
    top: 58px;
    height: 2px;
    background: var(--ink);
  }
  .label__rule--left { left: 24px; width: 218px; }
  .label__rule--right { right: 24px; width: 218px; }
  .label__seal {
    position: absolute;
    left: 247px;
    top: 21px;
    width: 76px;
    height: 76px;
  }
  .label__name {
    position: absolute;
    left: 0;
    right: 0;
    top: 120px;
    text-align: center;
    font-family: "Pinyon Script", cursive;
    font-size: 84px;
    line-height: 1;
    color: var(--gold);
  }
  .label__varietal {
    position: absolute;
    left: 0;
    right: 0;
    top: 262px;
    text-align: center;
    font-family: "Marcellus SC", serif;
    font-size: 24px;
    letter-spacing: 4px;
    color: var(--ink-soft);
  }
  .label__estate {
    position: absolute;
    left: 0;
    right: 0;
    top: 292px;
    text-align: center;
    font-family: "Kaushan Script", cursive;
    font-size: 30px;
    color: var(--ink);
  }
  .label__scene {
    position: absolute;
    left: 38px;
    top: 352px;
    width: 494px;
    height: 256px;
    border-radius: 18px 40px 22px 50px;
    background: linear-gradient(180deg, var(--scene-light) 0%, var(--scene-mid) 55%, var(--scene-dark) 100%);
  }
  .label__origin {
    position: absolute;
    left: 0;
    right: 0;
    top: 660px;
    text-align: center;
    font-family: "Cinzel", serif;
    font-weight: 500;
    font-size: 20px;
    letter-spacing: 5px;
    color: var(--ink);
  }
  .label__band {
    position: absolute;
    left: 0;
    right: 0;
    bottom: 6px;
    height: 22px;
    background: linear-gradient(180deg, var(--gold-deep) 0%, var(--gold-light) 45%, var(--gold) 100%);
  }
</style>
</head>
<body>
  <main class="canvas">
    <section class="label">
      <div class="label__rule label__rule--left"></div>
      <svg class="label__seal" viewBox="0 0 76 76" aria-hidden="true">
        <defs>
          <radialGradient id="sealGold" cx="40%" cy="35%" r="70%">
            <stop offset="0%" stop-color="#f3d77a"/>
            <stop offset="100%" stop-color="#b8861f"/>
          </radialGradient>
        </defs>
        <circle cx="38" cy="38" r="36" fill="url(#sealGold)"/>
      </svg>
      <div class="label__rule label__rule--right"></div>

      <h1 class="label__name">Cora Whitlow</h1>
      <p class="label__varietal">Reserve Pinot Noir</p>
      <p class="label__estate">Estate Grown</p>

      <div class="label__scene" role="img" aria-label="Black and white painted view of vineyard rows between a wooden barn and farm buildings, a large oak tree and a flock of birds on the horizon, with a tractor in the foreground"></div>

      <p class="label__origin">Clarksburg 2023</p>
      <div class="label__band"></div>
    </section>
  </main>
</body>
</html>
```